Aunt Rolina's Bakery

I am about to create a luxury boutique that specializes in cake baking and cupcake
and ready for parties and special events and order delivery
the logo has already made

Industry/Entity Type

Boutique

Contact Information for Business Card

Email:auntrolinasbakery@maplecrumbmail.com
Instagram: aunt_rolina_bakery
Twitter: xxxxxxx
WhatsApp: xxxxxxx

Requirements
Must have
• luxury design

```html
<!DOCTYPE html>
<html lang="en">
<head>
<meta charset="utf-8">
<title>Aunt Rolina's Bakery – Business Card</title>
<link rel="stylesheet" href="https://fonts.googleapis.com/css2?family=Alegreya+Sans:wght@400;700&display=swap">
<style>
  :root {
    --stage: #1c1c1c;
    --card-white: #ffffff;
    --slate: #7b7b74;
    --rose: #d898a9;
    --ink-grey: #7a7a74;
    --text-light: #ffffff;
  }
  * { box-sizing: border-box; margin: 0; padding: 0; }
  html, body {
    width: 1200px;
    height: 902px;
    overflow: hidden;
    background: var(--stage);
    font-family: "Alegreya Sans", sans-serif;
  }
  .business-card {
    position: absolute;
    left: 50px;
    top: 138px;
    width: 1100px;
    height: 625px;
    background: var(--card-white);
    overflow: hidden;
  }
  .card-shapes {
    position: absolute;
    inset: 0;
    width: 100%;
    height: 100%;
  }
  .brand-name {
    position: absolute;
    left: 40px;
    top: 288px;
    width: 430px;
    text-align: center;
    font-size: 40px;
    font-weight: 400;
    line-height: 1.1;
    color: var(--ink-grey);
  }
  .person {
    position: absolute;
    right: 46px;
    top: 72px;
    text-align: right;
  }
  .person-name {
    font-size: 46px;
    font-weight: 700;
    color: var(--text-light);
    line-height: 1;
  }
  .person-role {
    font-size: 31px;
    font-weight: 400;
    color: var(--rose);
    line-height: 1.1;
  }
  .contact-list {
    position: absolute;
    right: 46px;
    top: 377px;
    list-style: none;
  }
  .contact-item {
    display: flex;
    align-items: center;
    justify-content: flex-end;
    height: 38px;
    font-size: 29px;
    color: var(--text-light);
    white-space: nowrap;
  }
  .contact-icon {
    width: 29px;
    height: 29px;
    margin-left: 16px;
    background: var(--rose);
    flex: none;
  }
</style>
</head>
<body>
  <div class="business-card">
    <svg class="card-shapes" viewBox="0 0 941 535" preserveAspectRatio="none" aria-hidden="true">
      <rect class="panel-slate" x="0" y="0" width="941" height="535" fill="var(--slate)"/>
      <polygon class="divider-line" points="0,0 331,0 584,267.5 331,535 0,535" fill="var(--card-white)"/>
      <polygon class="chevron-band" points="0,0 327,0 580,267.5 327,535 0,535" fill="var(--rose)"/>
      <polygon class="panel-white" points="0,0 270,0 524,267.5 270,535 0,535" fill="var(--card-white)"/>
    </svg>

    <p class="brand-name">Aunt Rolina's Bakery</p>

    <div class="person">
      <p class="person-name">Employee Name</p>
      <p class="person-role">Managing Director</p>
    </div>

    <ul class="contact-list">
      <li class="contact-item">000-000-0000
        <svg class="contact-icon" viewBox="0 0 29 29" aria-label="Phone">
          <rect width="29" height="29" fill="var(--rose)"/>
          <path d="M9 8c1-1 2-1 3 0l1.5 2.5c.4.7 0 1.4-.6 1.8l-.9.6c.8 1.8 2.3 3.3 4.1 4.1l.6-.9c.4-.6 1.1-1 1.8-.6L21 17c1 1 1 2 0 3-1.5 1.5-4 1.5-7-1s-6-6-6-8.5c0-1 .3-1.8 1-2.5z" fill="var(--text-light)"/>
        </svg>
      </li>
      <li class="contact-item">aunt_rolina_bakery<span class="contact-icon"></span></li>
      <li class="contact-item">aunt_rolina_bakery<span class="contact-icon"></span></li>
      <li class="contact-item">aunt_rolina_bakery<span class="contact-icon"></span></li>
      <li class="contact-item">auntrolinasbakery@maplecrumbmail.com
        <svg class="contact-icon" viewBox="0 0 29 29" aria-label="Email">
          <rect width="29" height="29" fill="var(--rose)"/>
          <rect x="6" y="9" width="17" height="12" fill="none" stroke="var(--text-light)" stroke-width="1.6"/>
          <path d="M6 9l8.5 7L23 9" fill="none" stroke="var(--text-light)" stroke-width="1.6"/>
        </svg>
      </li>
    </ul>
  </div>
</body>
</html>
```